Marlow Glen Quilts

We are opening a long-arm quilting business where customers will bring in their pieced quilt top and have us quilt it to the batting and backing. We own a Brevant Ostrel Seamer - photos can be found on the internet. We would like for our business card and logo to include an image of a long arm quilting machine so that our business type would be easily recognizable. We like lots of color and contemporary styling, perhaps with colorful fabric flowing on the card as well. It needs to be something transferable to a store window and/or to a decal for our car to aid in advertising.

Industry/Entity Type

Store

Colors
fff5ee
fde8d3

```html
<!DOCTYPE html>
<html lang="en">
<head>
<meta charset="utf-8">
<title>Marlow Glen Quilts — Business Card</title>
<link href="https://fonts.googleapis.com/css2?family=Oswald:wght@700&display=swap" rel="stylesheet">
<style>
  :root {
    --stage: #2b2b2b;
    --ink-white: #ffffff;
    --fabric-navy: #1d2a8c;
    --fabric-blue: #2f6fd6;
    --fabric-sky: #7fc4f0;
    --fabric-yellow: #f7c51e;
    --fabric-orange: #f08a24;
    --fabric-magenta: #d93a9b;
    --fabric-green: #3fb94a;
    --fabric-violet: #6a3aa8;
  }
  * { margin: 0; padding: 0; box-sizing: border-box; }
  html, body {
    width: 1200px;
    height: 1008px;
    overflow: hidden;
    background: var(--stage);
  }
  .canvas {
    position: relative;
    width: 1200px;
    height: 1008px;
  }
  .business-card {
    position: absolute;
    left: 60px;
    top: 195px;
    width: 1080px;
    height: 617px;
    overflow: hidden;
  }
  .fabric-backdrop {
    position: absolute;
    inset: 0;
    background:
      linear-gradient(200deg, var(--fabric-green) 0%, rgba(63,185,74,0) 30%),
      linear-gradient(160deg, var(--fabric-magenta) 0%, var(--fabric-yellow) 22%, var(--fabric-orange) 34%, rgba(240,138,36,0) 48%),
      linear-gradient(20deg, var(--fabric-violet) 0%, var(--fabric-navy) 25%, var(--fabric-blue) 50%, var(--fabric-sky) 70%, var(--fabric-magenta) 100%);
  }
  .brand {
    position: absolute;
    left: 120px;
    top: 190px;
    display: flex;
    align-items: center;
    gap: 50px;
  }
  .brand-mark {
    width: 150px;
    height: 150px;
    background: var(--ink-white);
  }
  .brand-name {
    font-family: "Oswald", sans-serif;
    font-weight: 700;
    color: var(--ink-white);
    text-transform: uppercase;
    line-height: 0.95;
  }
  .brand-name-top {
    display: block;
    font-size: 140px;
    letter-spacing: 2px;
  }
  .brand-name-bottom {
    display: block;
    font-size: 92px;
    letter-spacing: 1px;
  }
</style>
</head>
<body>
  <main class="canvas">
    <section class="business-card">
      <div class="fabric-backdrop" role="img" aria-label="Colourful pieced quilt fabric in blues, yellows, magentas and greens radiating across the card"></div>
      <div class="brand">
        <div class="brand-mark"></div>
        <h1 class="brand-name">
          <span class="brand-name-top">Marlow</span>
          <span class="brand-name-bottom">Glen Quilts</span>
        </h1>
      </div>
    </section>
  </main>
</body>
</html>
```